81M business card

I need a business card for a life sciences consulting firm I started. The company name is 81M and the logo is attached. I am looking for something edgey and current but different from the blah standard business card.

Industry/Entity Type

Business

Requirements
Nice to have
• Both sides

```html
<!DOCTYPE html>
<html lang="en">
<head>
<meta charset="utf-8">
<title>81M Business Card</title>
<link href="https://fonts.googleapis.com/css2?family=Open+Sans:wght@300;400;600&display=swap" rel="stylesheet">
<style>
  :root {
    --backdrop: #e6e3df;
    --card-dark: #4b4e51;
    --card-light: #f4f4f4;
    --step-dark: #8d8f91;
    --step-light: #c9cacb;
    --text-light: #d2d3d4;
    --text-dark: #4a4a4a;
    --brand-orange: #e9761f;
    --brand-blue: #1f4f9e;
  }
  * { margin: 0; padding: 0; box-sizing: border-box; }
  html, body { width: 1200px; height: 723px; overflow: hidden; }
  body {
    background: var(--backdrop);
    font-family: "Open Sans", Arial, sans-serif;
    font-weight: 300;
    position: relative;
  }
  h1, h2, p { font-weight: inherit; }
  .card {
    position: absolute;
    top: 64px;
    width: 340px;
    height: 595px;
    overflow: hidden;
    box-shadow: 0 6px 18px rgba(0,0,0,0.18);
  }
  .card-front { left: 220px; background: var(--card-dark); }
  .card-back { left: 640px; background: var(--card-light); }

  .brand {
    position: absolute;
    display: flex;
    align-items: center;
    gap: 10px;
  }
  .brand-dot {
    width: 30px; height: 30px;
    border-radius: 50%;
  }
  .brand-name {
    font-size: 30px;
    font-weight: 400;
    letter-spacing: 1px;
  }
  .card-front .brand { left: 40px; top: 36px; }
  .card-front .brand-dot { background: var(--text-light); }
  .card-front .brand-name { color: var(--text-light); }

  .card-back .brand { right: 40px; top: 40px; }
  .card-back .brand-dot { background: var(--brand-orange); }
  .card-back .brand-name { color: var(--brand-blue); }
  .brand-tagline {
    position: absolute;
    right: 40px; top: 84px;
    font-size: 8px;
    font-weight: 400;
    color: var(--text-dark);
  }

  .service-title {
    font-weight: 300;
    line-height: 1.08;
    text-transform: uppercase;
    letter-spacing: 1px;
  }
  .card-front .service-title {
    position: absolute;
    left: 30px; bottom: 120px;
    font-size: 28px;
    color: var(--text-light);
  }
  .accent { color: var(--brand-orange); }

  .card-back .service-block {
    position: absolute;
    left: 40px; top: 228px;
    padding-left: 14px;
    border-left: 4px solid var(--brand-blue);
  }
  .card-back .service-title { font-size: 22px; color: var(--brand-blue); }
  .person { margin-top: 24px; }
  .person-name { font-size: 28px; color: var(--text-dark); line-height: 1.1; }
  .person-role { font-size: 14px; color: var(--brand-orange); }

  .contact {
    position: absolute;
    left: 40px; top: 410px;
    padding-left: 14px;
    border-left: 3px solid var(--brand-blue);
    font-size: 17px;
    font-weight: 400;
    line-height: 1.3;
  }
  .contact-phone { color: var(--brand-blue); }
  .contact-email { color: var(--text-dark); }
  .contact-web { color: var(--brand-orange); }

  .step-band {
    position: absolute;
    left: 0; bottom: 0;
    width: 340px; height: 60px;
  }
</style>
</head>
<body>

  <section class="card card-front">
    <div class="brand">
      <span class="brand-dot"></span>
      <span class="brand-name">81M LLC</span>
    </div>
    <h1 class="service-title">
      Regulatory<br>
      <span class="accent">Consulting</span> and<br>
      Contract <span class="accent">Services</span>
    </h1>
    <svg class="step-band" viewBox="0 0 340 60" aria-hidden="true">
      <path d="M0 24 H70 V10 H120 V24 H170 V10 H210 V30 H260 V14 H300 V30 H340 V60 H0 Z" fill="var(--step-dark)"/>
    </svg>
  </section>

  <section class="card card-back">
    <div class="brand">
      <span class="brand-dot"></span>
      <span class="brand-name">81M LLC</span>
    </div>
    <p class="brand-tagline">regulatory consulting and contract services</p>

    <div class="service-block">
      <h2 class="service-title">
        Regulatory<br>
        <span class="accent">Consulting</span> and<br>
        Contract <span class="accent">Services</span>
      </h2>
      <div class="person">
        <p class="person-name">Your Name</p>
        <p class="person-role">manager director</p>
      </div>
    </div>

    <div class="contact">
      <p class="contact-phone">+111 111 111</p>
      <p class="contact-email">hello@81m-advisory.net</p>
      <p class="contact-web">www.81m-advisory.net</p>
    </div>

    <svg class="step-band" viewBox="0 0 340 60" aria-hidden="true">
      <path d="M0 24 H70 V10 H120 V24 H170 V10 H210 V30 H260 V14 H300 V30 H340 V60 H0 Z" fill="var(--step-light)"/>
    </svg>
  </section>

</body>
</html>
```